Summer Drinks Flyer for Coffee Shop

We are a coffee shop in London and would like to have a cool and nice flyer for our summer drinks (juices and frozen drink) flyer - see on the attached file for the list

Attached you can find an "attempt" - please note that I would no necessary need the image below.

I also attache our new logo.

thank you

```html
<!DOCTYPE html>
<html lang="en">
<head>
<meta charset="utf-8">
<title>New Summer Drinks Menu</title>
<link rel="stylesheet" href="https://fonts.googleapis.com/css2?family=Luckiest+Guy&family=Titan+One&family=Alegreya+Sans+SC:wght@800&family=Arimo:wght@400;700&display=swap">
<style>
  :root {
    --bg-top: #f0a452;
    --bg-mid: #e6bc5e;
    --bg-lime: #d6ea7c;
    --bg-bottom: #98f54e;
    --heading-fill: #ffffff;
    --heading-stroke: #5ee03a;
    --sun-yellow: #f6ea4a;
    --sun-orange: #f5a623;
    --label-bg: #eef6b4;
    --frozen: #c0187a;
    --juice: #e8321e;
    --coffee: #6b4a22;
    --ink: #111111;
    --footer-frame: #3d9a2a;
    --footer-bg: #ffffff;
    --brand: #b8861e;
  }
  * { box-sizing: border-box; margin: 0; padding: 0; }
  html, body { width: 849px; height: 1200px; overflow: hidden; }
  body { background: #ffffff; }

  .flyer {
    position: relative;
    width: 849px;
    height: 1200px;
    overflow: hidden;
    background: linear-gradient(to bottom,
      var(--bg-top) 0%, var(--bg-top) 30%,
      var(--bg-mid) 48%, var(--bg-lime) 68%,
      var(--bg-bottom) 92%);
    font-family: "Arimo", Arial, sans-serif;
  }

  .sun-art {
    position: absolute;
    top: 42px;
    height: 302px;
    border-radius: 24px;
    background: linear-gradient(to bottom, var(--sun-yellow), var(--sun-orange) 55%, var(--sun-yellow));
    opacity: 0.85;
  }
  .sun-art--left { left: 57px; width: 301px; }
  .sun-art--right { left: 509px; width: 293px; }

  .title {
    position: absolute;
    left: 0; right: 0;
    text-align: center;
    font-family: "Luckiest Guy", "Titan One", "Arial Black", cursive;
    font-weight: 400;
    color: var(--heading-fill);
    -webkit-text-stroke: 8px var(--heading-stroke);
    paint-order: stroke fill;
    line-height: 1;
    letter-spacing: 2px;
  }
  .title--top { top: 92px; font-size: 84px; transform: rotate(-3deg); }
  .title--bottom { top: 222px; font-size: 90px; letter-spacing: 0; }

  .drink-art {
    position: absolute;
    border-radius: 16px;
  }
  .drink-art--frozen {
    left: 38px; top: 434px; width: 113px; height: 245px;
    background: linear-gradient(to bottom, #8fdc5a, #3fae22);
  }
  .drink-art--juice {
    left: 38px; top: 787px; width: 165px; height: 274px;
    background: linear-gradient(to bottom, #f9c27a, #f2982c);
  }

  .section { position: absolute; left: 0; width: 849px; }
  .section__label {
    position: absolute;
    height: 59px;
    background: var(--label-bg);
    font-family: "Alegreya Sans SC", "Copperplate", sans-serif;
    font-weight: 800;
    font-size: 35px;
    line-height: 59px;
    letter-spacing: 1.5px;
    padding-left: 12px;
  }
  .section__price {
    position: absolute;
    width: 84px; height: 84px;
    border-radius: 50%;
    background: var(--label-bg);
    font-family: "Luckiest Guy", "Titan One", "Arial Black", cursive;
    font-weight: 400;
    font-size: 28px;
    line-height: 90px;
    text-align: center;
  }
  .section__items {
    position: absolute;
    list-style: none;
    font-weight: 700;
    font-size: 24px;
    line-height: 32px;
    color: var(--ink);
  }

  .section--frozen .section__label { left: 228px; top: 433px; width: 383px; color: var(--frozen); }
  .section--frozen .section__price { left: 708px; top: 420px; color: var(--frozen); }
  .section--frozen .section__items { left: 230px; top: 507px; }

  .section--juice .section__label { left: 228px; top: 608px; width: 259px; color: var(--juice); }
  .section--juice .section__price { left: 703px; top: 595px; color: var(--juice); }
  .section--juice .section__items { left: 233px; top: 687px; }

  .section--coffee .section__label { left: 234px; top: 886px; width: 271px; color: var(--coffee); }
  .section--coffee .section__price { left: 708px; top: 873px; color: var(--coffee); }
  .section--coffee .section__items { left: 238px; top: 962px; }

  .footer {
    position: absolute;
    left: 0; top: 1094px;
    width: 849px; height: 106px;
    background: var(--footer-bg);
    border: 6px solid var(--footer-frame);
  }
  .extra {
    position: absolute;
    left: 14px;
    display: flex;
    align-items: center;
  }
  .extra--juice { top: 10px; }
  .extra--coffee { top: 55px; }
  .extra__name {
    width: 132px;
    font-family: "Alegreya Sans SC", "Copperplate", sans-serif;
    font-weight: 800;
    font-size: 19px;
    letter-spacing: 1px;
  }
  .extra--juice .extra__name { color: var(--juice); }
  .extra--coffee .extra__name { color: var(--coffee); }
  .extra__arrow { width: 44px; height: 20px; margin-right: 30px; }
  .extra--juice .extra__arrow { margin-left: 6px; }
  .extra--coffee .extra__arrow { margin-left: 14px; margin-right: 22px; }
  .extra__note {
    font-weight: 700;
    font-size: 14px;
    line-height: 16px;
    color: var(--ink);
  }

  .brand {
    position: absolute;
    right: 34px; top: 28px;
    font-family: "Arimo", Arial, sans-serif;
    font-weight: 400;
    font-size: 38px;
    color: var(--brand);
    letter-spacing: 1px;
  }
</style>
</head>
<body>
<main class="flyer">
  <div class="sun-art sun-art--left" role="img" aria-label="Cartoon sun illustration"></div>
  <div class="sun-art sun-art--right" role="img" aria-label="Cartoon sun illustration"></div>

  <h1>
    <span class="title title--top">NEW SUMMER</span>
    <span class="title title--bottom">DRINKS MENU</span>
  </h1>

  <div class="drink-art drink-art--frozen" role="img" aria-label="Illustration of a frozen fruit drink"></div>
  <div class="drink-art drink-art--juice" role="img" aria-label="Illustration of a glass of orange juice"></div>

  <section class="section section--frozen">
    <h2 class="section__label">Frozen Fruit Drinks</h2>
    <p class="section__price">£2.95</p>
    <ul class="section__items">
      <li>Strawberry and Banana</li>
      <li>Pineapple, Mango and Banana</li>
    </ul>
  </section>

  <section class="section section--juice">
    <h2 class="section__label">Fruit Juices</h2>
    <p class="section__price">£2.95</p>
    <ul class="section__items">
      <li>Orange and Carrot</li>
      <li>Orange and Pineapple</li>
      <li>Pineapple and Apple</li>
      <li>Apple and Kiwi</li>
      <li>Carrot and Ginger</li>
    </ul>
  </section>

  <section class="section section--coffee">
    <h2 class="section__label">Iced- Coffees</h2>
    <p class="section__price">£2.45</p>
    <ul class="section__items">
      <li>Iced Coffe</li>
      <li>Iced Latte</li>
      <li>Iced Chocolate Drink</li>
    </ul>
  </section>

  <footer class="footer">
    <div class="extra extra--juice">
      <span class="extra__name">Fruit Juices</span>
      <svg class="extra__arrow" viewBox="0 0 44 20" aria-hidden="true">
        <line x1="0" y1="10" x2="30" y2="10" stroke="#000" stroke-width="4"/>
        <polygon points="26,2 44,10 26,18" fill="#000"/>
      </svg>
      <p class="extra__note">Add Minter or Ginger<br>For Free!</p>
    </div>
    <div class="extra extra--coffee">
      <span class="extra__name">Iced- Coffees</span>
      <svg class="extra__arrow" viewBox="0 0 44 20" aria-hidden="true">
        <line x1="0" y1="10" x2="30" y2="10" stroke="#000" stroke-width="4"/>
        <polygon points="26,2 44,10 26,18" fill="#000"/>
      </svg>
      <p class="extra__note">Add Syrup Shot<br>For 10 p</p>
    </div>
    <p class="brand">solenne</p>
  </footer>
</main>
</body>
</html>
```